The Willowbank Clinic :

At The Willowbank Clinic our goal is to provide the most skilled and advanced examination and treatment of the upper neck for superior long-term outcomes for those experiencing headache or migraine.

If a spinal disorder is responsible for the headache and migraine condition the disorder will involve one or more of the top three spinal segments. The fundamental and most powerful feature of The Willowbank Clinic is our method of examining the movements of the top three spinal segments.

We would like the design should communicate professionalism and specialisation.
Updates

Don't necessarily have to have the photos provided.Photo was used for promotional material. I dont have a logo as yet what I  would also like designed.

Project Deadline Extended
Reason: Opening has been delayed due to construction issues of building.

Industry/Entity Type

Clinic

Contact Information for Business Card

The Willowbank Clinic
Suite 4, Larchford Heath Centre
87 Tollbury Drive, Harlow Bay NSW 2471
Tel : 63 27 1846 www.thewillowbankclinic.com.au

Requirements
Must have
• Mr Colin Hartwell
Senior Physiotherapist / Senior Accredited Exercise Physiologist
B. Hlth Sc. (Physiotherapy), B. Mov. Sc. (Exercise Science), Grad. Dip. R.T, MRTA, MUPGA, MVTB, MBRLK.

Appointment area on back of card

```html
<!DOCTYPE html>
<html lang="en">
<head>
<meta charset="utf-8">
<title>The Willowbank Clinic – Business Card</title>
<link rel="stylesheet" href="https://fonts.googleapis.com/css2?family=Questrial&family=PT+Sans:ital,wght@0,400;0,700;1,400&family=PT+Sans+Narrow&family=Cinzel:wght@500&family=Courgette&display=swap">
<style>
  :root {
    --purple: #6a2c86;
    --green: #8dc63f;
    --deep-green: #2f6b34;
    --ink: #333333;
    --line: #555555;
    --card: #ffffff;
    --backdrop: #e9e6e2;
  }
  * { box-sizing: border-box; margin: 0; padding: 0; }
  html, body {
    width: 1200px; height: 1130px; overflow: hidden;
    background: var(--backdrop);
  }
  .canvas { position: relative; width: 1200px; height: 1130px; }

  .card {
    position: absolute;
    width: 780px; height: 470px;
    background: var(--card);
    border-radius: 30px;
    overflow: hidden;
    box-shadow: 0 8px 24px rgba(0,0,0,0.18);
  }
  .card--front { left: 90px; top: 70px; }
  .card--back { left: 330px; top: 590px; }

  /* Front */
  .front-text {
    position: absolute; left: 0; right: 0; text-align: center;
    font-family: 'Questrial', sans-serif; font-weight: 400;
  }
  .clinic-name { top: 36px; font-size: 54px; color: var(--purple); }
  .practitioner { top: 126px; font-size: 29px; color: var(--purple); }
  .credentials {
    top: 168px; padding: 0 80px;
    font-family: 'PT Sans Narrow', sans-serif;
    font-size: 20px; line-height: 1.22; color: var(--green);
  }
  .phone { top: 262px; font-size: 34px; color: var(--purple); }
  .address { top: 318px; font-size: 18px; line-height: 1.35; color: var(--purple); }
  .band { position: absolute; left: 0; top: 0; width: 780px; height: 470px; }
  .website { top: 418px; font-size: 25px; letter-spacing: 2px; color: #ffffff; }

  /* Back */
  .tagline {
    position: absolute; left: 42px; top: 20px;
    font-family: 'Courgette', cursive; font-size: 28px; color: #111111;
  }
  .back-clinic-name {
    position: absolute; right: 40px; top: 66px;
    font-family: 'Questrial', sans-serif; font-weight: 400;
    font-size: 38px; color: var(--purple);
  }
  .appointment-heading {
    position: absolute; left: 70px; top: 112px;
    font-family: 'Cinzel', serif; font-weight: 500; font-size: 24px; color: var(--deep-green);
  }
  .form-row {
    position: absolute; left: 60px; right: 40px;
    display: flex; align-items: flex-end; gap: 10px;
    font-family: 'PT Sans', sans-serif; font-size: 21px; color: var(--ink);
  }
  .field-line { border-bottom: 1.5px dotted var(--line); height: 1px; margin-bottom: 6px; }
  .field-line--solid { border-bottom-style: solid; }
  .row-name { top: 160px; left: 72px; }
  .row-date { top: 212px; }
  .row-next { top: 262px; align-items: center; }
  .row-days { top: 330px; left: 48px; align-items: center; gap: 8px; font-weight: 700; font-size: 20px; }
  .box { width: 135px; height: 34px; border: 1.5px solid var(--line); border-radius: 3px; }
  .day-box { width: 46px; height: 32px; border: 1.5px solid var(--line); border-radius: 3px; margin-right: 14px; }
  .cancellation-note {
    position: absolute; left: 48px; top: 392px;
    font-family: 'PT Sans', sans-serif; font-style: italic; font-size: 19px; color: var(--ink);
  }
</style>
</head>
<body>
<main class="canvas">

  <section class="card card--front" aria-label="Business card front">
    <svg class="band" viewBox="0 0 780 470" aria-hidden="true">
      <path d="M0 356 Q390 440 780 344 L780 356 Q390 432 0 378 Z" fill="var(--green)"/>
      <path d="M0 386 Q390 452 780 360 L780 470 L0 470 Z" fill="var(--purple)"/>
    </svg>
    <h1 class="front-text clinic-name">The Willowbank Clinic</h1>
    <p class="front-text practitioner">Mr Colin Hartwell</p>
    <p class="front-text credentials">Senior Physiotherapist / Senior Accredited Exercise Physiologist B. Hlth Sc.<br>(Physiotherapy), B. Mov. Sc. (Exercise Science), Grad. Dip. R.T,<br>MRTA, MUPGA, MVTB, MBRLK.</p>
    <p class="front-text phone">Tel : 63 27 1846</p>
    <p class="front-text address">Suite 4, Larchford Heath Centre 87<br>Tollbury Drive, Harlow Bay NSW 2471</p>
    <p class="front-text website">www.thewillowbankclinic.com.au</p>
  </section>

  <section class="card card--back" aria-label="Business card back">
    <p class="tagline">picture each day free of headaches</p>
    <h2 class="back-clinic-name">The Willowbank Clinic</h2>
    <h3 class="appointment-heading">Your Appointment</h3>

    <div class="form-row row-name">
      <span>Name :</span><span class="field-line" style="width:420px"></span>
    </div>
    <div class="form-row row-date">
      <span>Date :</span><span class="field-line field-line--solid" style="width:130px"></span>
      <span>Time :</span><span class="field-line field-line--solid" style="width:125px"></span>
      <span>am / pm</span>
    </div>
    <div class="form-row row-next">
      <span>Next Appointment</span><span class="box"></span><span class="box" style="margin-left:6px"></span>
    </div>
    <div class="form-row row-days">
      <span>MON</span><span class="day-box"></span>
      <span>TUE</span><span class="day-box"></span>
      <span>WED</span><span class="day-box"></span>
      <span>THU</span><span class="day-box"></span>
      <span>FRI</span><span class="day-box"></span>
      <span>SAT</span><span class="day-box"></span>
    </div>
    <p class="cancellation-note">We appreciate a 24 hr. notice for cancellations</p>
  </section>

</main>
</body>
</html>
```